Law firm website marketed direct to many individual clients

I need someone to design a very basic website for a law firm that will be very eye catching. It's going to be a single-paged, scrolling website with a small number of folds. I have uploaded a simple word document that outlines the basics of what I thought could be the layout, but I am open to suggestion on font, size, shades of color, organization, etc. etc. Essentially the website just needs to be a very efficient and visually appealing way of conveying some simple messages.

Target Market(s)

High volumes of individuals who have gotten into a car accident and then google on their phones a lawyer to hire to represent them.

Industry/Entity Type

Legal

Number of Pages Required

1 page

Font styles to use
Serif
Sans Serif

Colors
34a7d7
85cae6
0592cd

Requirements
Must have
• Must be bright and grab the users attention with color scheme and layout. The different sections should be done in such a way that they can fit entirely onto one smart phone or tablet screen.
Nice to have
• I'd like to try and see what it looks like if in the middle somewhere there is a fold that says "MEET YOUR ATTORNEYS" and includes individual photos of two attorneys, one on the left side and one on the right. And then a small bio section on them. I don't want the photos to include a square or rectangle background, I want the person in the photo to be superimposed on top of whatever pattern or background you have in the fold.
Should not have
• Do not want too much text. Anything more than 2 sentences in any single place is unacceptable.

```html
<!DOCTYPE html>
<html lang="en">
<head>
<meta charset="utf-8">
<title>Harborline Law Group</title>
<link href="https://fonts.googleapis.com/css2?family=Arimo:wght@400;700&display=swap" rel="stylesheet">
<style>
:root{
  --brand:#0a8fcd;
  --brand-mid:#34a7d7;
  --brand-light:#85cae6;
  --hero-dark:#0c4f78;
  --hero-mid:#17679a;
  --navy:#0e3554;
  --ink:#333;
  --grey:#777;
  --white:#fff;
}
*{margin:0;padding:0;box-sizing:border-box}
html,body{width:1200px;height:3041px;overflow:hidden;background:var(--white)}
body{font-family:"Arimo",Arial,sans-serif;position:relative}
.abs{position:absolute}
.center{left:0;width:1200px;text-align:center}

/* hero */
.hero{position:absolute;left:0;top:0;width:1200px;height:738px;overflow:hidden}
.hero-bg{position:absolute;inset:0;background:radial-gradient(ellipse at 50% 45%,var(--hero-mid) 0%,var(--hero-dark) 75%)}
.hero-monument{position:absolute;left:400px;top:0;width:330px;height:738px;background:linear-gradient(180deg,rgba(255,255,255,.08),rgba(255,255,255,.14) 60%,rgba(0,0,0,.1));}
.brand-name{top:258px;font-size:68px;letter-spacing:9px;color:var(--white);font-weight:400}
.brand-sub{top:344px;font-size:36px;letter-spacing:6px;color:var(--white)}
.hero-phone{left:405px;top:418px;width:388px;height:50px;background:var(--white);display:flex;align-items:center;justify-content:center;gap:18px;color:var(--brand);font-size:35px;letter-spacing:3px;box-shadow:0 3px 6px rgba(0,0,0,.25)}
.hero-phone svg{width:30px;height:30px}
.scroll-cue{left:582px;top:640px;width:36px;height:73px;border:3px solid var(--white);border-radius:18px;display:flex;align-items:center;justify-content:center}

/* call-to-action stack */
.btn{position:absolute;left:405px;width:388px;background:var(--brand);color:var(--white);text-align:center;box-shadow:0 3px 5px rgba(0,0,0,.2);letter-spacing:3px;display:flex;flex-direction:column;align-items:center;justify-content:center}
.btn-std{height:50px;font-size:27px}
.btn-call{font-size:26px;letter-spacing:2px}
.btn-call b{font-weight:400;font-size:31px;letter-spacing:2px;margin-left:8px}
.btn-big{height:107px;font-size:28px;line-height:1.4}
.btn-big strong{font-size:32px;font-weight:700;letter-spacing:4px}
.btn-white{background:var(--white);color:var(--brand)}

/* attorneys */
.team-title{left:282px;top:1285px;width:640px;height:53px;background:var(--brand);color:var(--white);font-size:30px;letter-spacing:2px;display:flex;align-items:center;justify-content:center}
.portrait{top:1340px;width:262px;height:284px;background:linear-gradient(180deg,#e6e6e6,#c9c9c9)}
.team-divider{left:598px;top:1340px;width:4px;height:284px}
.attorney{top:1636px;width:330px;text-align:center}
.attorney-name{color:var(--brand);font-size:20px;letter-spacing:2px}
.attorney-meta{color:var(--brand-mid);font-size:11px;letter-spacing:1px;line-height:17px;margin-top:6px}
.attorney-bio{color:var(--grey);font-size:11.5px;letter-spacing:1px;line-height:17px;margin-top:6px}

/* benefits */
.benefit-title{font-size:22px;letter-spacing:3px;color:var(--brand)}
.benefit-text{font-size:16px;letter-spacing:3px;color:var(--ink)}
.rule{left:440px;width:320px;height:6px}

/* info band */
.info{position:absolute;left:0;top:2382px;width:1200px;height:470px;background:var(--brand-light)}
.info-title{font-size:28px;letter-spacing:4px;color:var(--navy)}
.info-text{font-size:18px;letter-spacing:2px;color:var(--white);line-height:26.5px}

/* footer */
.footer{position:absolute;left:0;top:2852px;width:1200px;height:189px;background:var(--brand)}
.footer-lines{top:54px;font-size:16px;letter-spacing:3px;line-height:23.5px;color:var(--white)}
.to-top{left:1131px;top:111px;width:37px;height:44px;border:2px solid var(--white);display:flex;align-items:center;justify-content:center}
</style>
</head>
<body>

<header class="hero">
  <div class="hero-bg" role="img" aria-label="Photograph of a monument against a cloudy sky, tinted blue"></div>
  <div class="hero-monument" role="img" aria-label="Monument statue and stone pedestal"></div>
  <h1 class="abs center brand-name">Harborline</h1>
  <p class="abs center brand-sub">Law Group</p>
  <div class="abs hero-phone">
    <svg viewBox="0 0 30 30" aria-hidden="true"><rect width="30" height="30" rx="4" fill="#0a8fcd"/><path d="M10 7c1 0 2 3 2.5 4s-1.5 2-1.5 2.5 2.5 4.5 4.5 5 1.5-1.5 2.5-1.5 4 2 4 2.5-1.5 3.5-3 3.5C12 23 7 17 7 11c0-2 2-4 3-4z" fill="#fff"/></svg>
    <span>504-555-0187</span>
  </div>
  <div class="abs scroll-cue">
    <svg width="16" height="40" viewBox="0 0 16 40" aria-hidden="true"><path d="M8 2v34M2 29l6 8 6-8" stroke="#fff" stroke-width="2.5" fill="none"/></svg>
  </div>
</header>

<main>
  <div class="btn btn-std" style="top:801px">ACCIDENT?</div>
  <div class="btn btn-std" style="top:878px">INJURED?</div>
  <div class="btn btn-big" style="top:957px"><span>YOUR CASE</span><strong>YOUR MONEY</strong></div>
  <div class="btn btn-std btn-call" style="top:1093px;flex-direction:row">Call :<b>504-555-0187</b></div>
  <div class="btn btn-std" style="top:1170px;flex-direction:row;font-size:27px">Learn More
    <svg width="28" height="20" viewBox="0 0 28 20" style="margin-left:8px" aria-hidden="true"><path d="M3 3l7 7-7 7M14 3l7 7-7 7" stroke="#fff" stroke-width="3.5" fill="none"/></svg>
  </div>

  <section>
    <h2 class="abs team-title">Meet Your Attorneys</h2>
    <div class="abs portrait" style="left:282px" role="img" aria-label="Portrait of attorney Daniel Reyes in a grey suit"></div>
    <svg class="abs team-divider" viewBox="0 0 4 284" preserveAspectRatio="none" aria-hidden="true">
      <defs><linearGradient id="fade" x1="0" y1="0" x2="0" y2="1"><stop offset="0" stop-color="#34a7d7" stop-opacity="0"/><stop offset=".5" stop-color="#34a7d7"/><stop offset="1" stop-color="#34a7d7" stop-opacity="0"/></linearGradient></defs>
      <rect x="1.5" width="1" height="284" fill="url(#fade)"/><circle cx="2" cy="142" r="2" fill="#0a8fcd"/>
    </svg>
    <div class="abs portrait" style="left:659px" role="img" aria-label="Portrait of attorney Owen Carter in a pinstripe suit"></div>

    <div class="abs attorney" style="left:248px">
      <h3 class="attorney-name">Mr. Daniel Reyes</h3>
      <p class="attorney-meta">Person Qualification<br>Attorneys Degree<br>Profession Level</p>
      <p class="attorney-bio">Focused on injury claims and fair settlements<br>for local drivers. Known for clear advice<br>and quick calls back.</p>
    </div>
    <div class="abs attorney" style="left:626px">
      <h3 class="attorney-name">Mr. Owen Carter</h3>
      <p class="attorney-meta">Person Qualification<br>Attorneys Degree<br>Profession Level</p>
      <p class="attorney-bio">Handles crash cases from first call to final check.<br>Trusted by families across the region<br>for honest, steady help.</p>
    </div>
  </section>

  <section>
    <h3 class="abs center benefit-title" style="top:1823px">LOW FEES</h3>
    <p class="abs center benefit-text" style="top:1858px">We charge less, so you keep more.</p>
    <svg class="abs rule" style="top:1907px" viewBox="0 0 320 6" aria-hidden="true"><use href="#rule"/></svg>

    <h3 class="abs center benefit-title" style="top:1940px">FREE CONSULTATION</h3>
    <p class="abs center benefit-text" style="top:1976px">It's always free to talk to us.</p>
    <svg class="abs rule" style="top:2024px" viewBox="0 0 320 6" aria-hidden="true"><use href="#rule"/></svg>

    <h3 class="abs center benefit-title" style="top:2056px">GET STARTED USING ONLY YOUR PHONE</h3>
    <p class="abs center benefit-text" style="top:2093px">No need to come to the office, sign up using your phone.</p>
    <svg class="abs rule" style="top:2140px" viewBox="0 0 320 6" aria-hidden="true"><use href="#rule"/></svg>

    <h3 class="abs center benefit-title" style="top:2173px">SPEAK DIRECTLY TO A LAWYER</h3>
    <p class="abs center benefit-text" style="top:2209px">No staff screening. Talk right to a lawyer on your first call.</p>

    <div class="btn btn-std btn-call" style="top:2266px;flex-direction:row">Call :<b>504-555-0187</b></div>
  </section>
</main>

<svg width="0" height="0" style="position:absolute" aria-hidden="true">
  <defs>
    <linearGradient id="ruleGrad" x1="0" x2="1"><stop offset="0" stop-color="#34a7d7" stop-opacity="0"/><stop offset=".5" stop-color="#34a7d7"/><stop offset="1" stop-color="#34a7d7" stop-opacity="0"/></linearGradient>
    <g id="rule"><rect x="0" y="2.5" width="150" height="1" fill="url(#ruleGrad)"/><rect x="170" y="2.5" width="150" height="1" fill="url(#ruleGrad)"/><circle cx="160" cy="3" r="3" fill="#0a8fcd"/></g>
  </defs>
</svg>

<section class="info">
  <h2 class="abs center info-title" style="top:46px">NO FEE UNLESS WE WIN</h2>
  <p class="abs center info-text" style="top:82px">We don't get paid unless you get paid. It's as simple as that.<br>We let our results do the talking for us.</p>
  <h2 class="abs center info-title" style="top:175px">QUESTIONS ABOUT ANYTHING?</h2>
  <p class="abs center info-text" style="top:211px">We're here to help.<br>Feel free to call us at <b><i>504-555-0187</i></b> to speak to one of our attorneys.<br>With extensive experience in helping clients get the results that they want,<br>our team is always just a phone call away.</p>
  <div class="btn btn-std btn-call btn-white" style="top:364px;flex-direction:row">Call :<b>504-555-0187</b></div>
</section>

<footer class="footer">
  <p class="abs center footer-lines">Harborline Law Group<br>Riverside Office Suite<br>Harbor City, LA 70000<br>504-555-0187</p>
  <div class="abs to-top">
    <svg width="18" height="26" viewBox="0 0 18 26" aria-hidden="true"><path d="M9 24V3M3 10l6-7 6 7" stroke="#fff" stroke-width="2.5" fill="none"/></svg>
  </div>
</footer>

</body>
</html>
```